Flyer Design Project for Retailer

We are an indepedant retailer in the UK, selling Ladies, Mens & Kids Clothing, Homewares & Gifts.

Periodically we mail out a flyer to our customer database. This entitles the customer to a 10% discount along with any specific message/theme. For example; new season launch, etc.

We promote the flyer as a shopping card as it has a credit card size perforated pop out. This allows the customer to reuse the discount again and again within the time limit. It also gives the customer a sense of exclusivity.

Given the strong response we are also going to mail to similar postal addresses obtained from the postal register. These purchased addresses will not have a customer name therefore we need to capture the name upon the customer using their discount flyer. The design needs to allow for such capture.

Flyer Details
-style of flyer is to appreciate Autumn Season and to promote new autumn season stocks are now in.
-A5 double sided flyer, digitally printed and personalised
-Die cut out size; 85mm x 55mm (perforated pop out)
-Our cutomers are mainly female, however, design to appeal to male also.

Attachments:
-Halloways logo
-Cafe Lumino logo
-Opening times, terms & conditions, address/contact details.
Updates

Project Deadline Extended
Reason: To allow for more designers to submit their designs.

Project Deadline Extended
Reason: Require more ideas

Target Market(s)

-Existing Customers
-New Customers from same demographics of existing customers
-Mainly female customers, between ages 20-70.

Industry/Entity Type

Credit Card

Requirements
Must have
• -style of flyer is to appreciate Autumn Season and to promote new autumn season stocks are now in.
-Area for Customers name, address & PPI on main flyer
-Promote free parking
-Promote Cafe Lumino offering Breakfast, Lunch & Afternoon Tea
-Promote no membership is required to shop
-To include address/contact details (see attached details)
-To include terms & conditions (see attached text).
-To include opening times (see below)
-To promote new floor of Homewares & Ladies.
-Promote that discount is only valid until 30th October (date to be confirmed)

Clearly advertise that:
-customer gets 10% off everything.

Pop out card to include:
-Logos; Halloways & Cafe Lumino
-Area for customer name, barcode, postcode
-State that its a Shopping Card
-state that they will get 10% off
-Valid until date.

-Final artwork to be available in pdf, ready for printing and also orignal files.
-Amendments to chosen design to be allowed for in project price.

```html
<!DOCTYPE html>
<html lang="en">
<head>
<meta charset="utf-8">
<title>Halloways Autumn Shopping Card Flyer</title>
<link href="https://fonts.googleapis.com/css2?family=Lobster&family=Passion+One:wght@400;700&family=Fira+Sans:wght@400;600&family=Fira+Sans+Extra+Condensed:wght@700&display=swap" rel="stylesheet">
<style>
:root{
  --orange:#f39324;
  --brown:#5a1d14;
  --rust:#9b2f16;
  --olive:#6f7c33;
  --white:#ffffff;
  --page:#ffffff;
  --ink:#2b1a14;
  --placeholder-a:#f6e3cc;
  --placeholder-b:#ecd0b0;
}
*{box-sizing:border-box;margin:0;padding:0}
html,body{width:1200px;height:900px;overflow:hidden;background:var(--page)}
body{position:relative;font-family:"Fira Sans",Arial,sans-serif;color:var(--ink)}
.flyer{position:absolute;background:var(--white);box-shadow:3px 4px 10px rgba(0,0,0,.35);overflow:hidden}
.flyer--front{left:25px;top:15px;width:525px;height:730px}
.flyer--back{left:575px;top:130px;width:515px;height:710px}

.title-band{height:100px;display:flex;align-items:center;justify-content:center}
.title-band--orange{background:var(--orange);margin-top:15px}
.title-band--brown{background:var(--brown);height:95px}
.script-title{font-family:"Lobster",cursive;font-size:54px;paint-order:stroke fill}
.title-band--orange .script-title{color:var(--rust);-webkit-text-stroke:8px var(--white)}
.title-band--brown .script-title{color:var(--orange);-webkit-text-stroke:8px var(--white)}

.offer{position:relative;text-align:center;margin-top:20px}
.offer-illustration{position:absolute;left:100px;top:60px;width:82px;height:72px;border-radius:8px;background:linear-gradient(160deg,var(--placeholder-a),var(--placeholder-b))}
.offer-headline{font-family:"Passion One",sans-serif;font-weight:700;color:var(--olive);line-height:.9;-webkit-text-stroke:6px var(--white);paint-order:stroke fill;text-shadow:0 0 1px var(--rust)}
.offer-headline span{display:block}
.offer-headline .l1{font-size:70px;padding-left:70px}
.offer-headline .l2{font-size:76px;padding-left:60px}
.offer-headline .l3{font-size:80px;padding-left:50px}
.offer-note{font-family:"Passion One",sans-serif;font-size:32px;color:var(--rust);background:var(--white);display:inline-block;margin-left:40px;margin-top:2px;padding:0 6px;border:2px solid var(--orange)}

.new-floor{font-family:"Fira Sans Extra Condensed",sans-serif;font-weight:700;font-size:38px;line-height:1.05;color:var(--rust);text-align:center;margin-top:34px;padding-left:40px}

.card-strip{position:absolute;left:0;right:0;bottom:0;height:225px;display:flex}
.panel-brown{background:var(--brown);color:var(--white)}
.panel-orange{background:var(--orange);position:relative}
.perforation{position:absolute;inset:6px;border:1.5px dashed var(--brown);pointer-events:none}

.front-address{width:220px;padding:20px 10px 0;text-align:center}
.front-address .address{font-size:13.5px;line-height:1.35;white-space:nowrap}
.offer-date{font-size:9.5px;margin-top:12px;white-space:nowrap}
.terms{font-size:8.5px;line-height:1.25;margin-top:10px}

.front-card{flex:1;text-align:center;padding:20px 18px 0}
.card-heading{font-family:"Passion One",sans-serif;font-size:29px;color:var(--brown);line-height:1.15}
.brand-row{display:flex;justify-content:center;gap:32px;margin-top:28px}
.brand-name{font-family:"Fira Sans",Arial,sans-serif;font-weight:600;font-size:20px;color:var(--brown)}
.card-small{font-size:8.5px;line-height:1.3;color:var(--brown);margin-top:20px;padding:0 4px}

.cafe-brand{text-align:center;margin-top:28px;font-weight:600;font-size:30px;color:var(--brown)}
.serving{text-align:center;font-family:"Passion One",sans-serif;font-size:27px;color:var(--brown);margin-top:18px}
.serving b{color:var(--orange);font-weight:400}
.times-heading{text-align:center;font-family:"Passion One",sans-serif;font-size:27px;color:var(--orange);margin-top:22px}
.times{text-align:center;margin-top:16px}
.times h3{font-family:"Passion One",sans-serif;font-weight:400;font-size:30px;color:var(--brown);line-height:1}
.times p{font-size:12.5px;line-height:1.3}
.parking{text-align:center;font-family:"Passion One",sans-serif;font-weight:700;font-size:68px;color:var(--orange);-webkit-text-stroke:3px var(--brown);paint-order:stroke fill;margin-top:16px;line-height:1}

.back-strip{height:205px}
.back-card{width:290px;text-align:center;padding-top:22px;color:var(--white)}
.back-card .address{font-size:14px;line-height:1.35}
.back-card .brand-name{display:block;margin-top:48px;font-size:24px}
.valid{font-size:9px;color:var(--brown);margin-top:4px}
.contact{flex:1;text-align:center;padding-top:28px}
.contact h4{font-weight:400;font-size:22px;margin-bottom:16px}
.contact p{font-size:13px;line-height:1.35}
</style>
</head>
<body>

<section class="flyer flyer--front">
  <header class="title-band title-band--orange"><h1 class="script-title">Autumn Arrivals</h1></header>
  <div class="offer">
    <div class="offer-illustration" role="img" aria-label="Small autumn bird illustration"></div>
    <h2 class="offer-headline"><span class="l1">Get 10%</span><span class="l2">OFF</span><span class="l3">EVERYTHING*</span></h2>
    <p class="offer-note">No Membership Required</p>
  </div>
  <p class="new-floor">Be Sure To See Our NEW<br>Homewares &amp; Ladies Floor!</p>
  <div class="card-strip">
    <div class="panel-brown front-address">
      <p class="address">Clara Benton<br>48 Halloways Court<br>Riverside, Melbourne, Vic, 3010</p>
      <p class="offer-date">*Discount Offer Effective Until 30th October</p>
      <p class="terms">Terms &amp; Conditions:<br>10% discount applies to all purchases made in Halloways &amp; Cafe Lumino, up until and including Sat 30th October 2011. Vouchers are limited to one per customer and cannot be used in conjunction with any other offer. This voucher has no cash value. We reserve the right to cancel this voucher at any time, without notice.</p>
    </div>
    <div class="panel-orange front-card">
      <span class="perforation"></span>
      <h3 class="card-heading">Your Personal<br>Shopping Card</h3>
      <div class="brand-row"><span class="brand-name">Cafe Lumino</span><span class="brand-name">Halloways</span></div>
      <p class="card-small">This card entitles you to enjoy 10% off your purchases at Halloways</p>
    </div>
  </div>
</section>

<section class="flyer flyer--back">
  <header class="title-band title-band--brown"><h2 class="script-title">Stay for a Bite</h2></header>
  <p class="cafe-brand">Cafe Lumino</p>
  <p class="serving"><b>Serving:</b> Breakfast, Lunch &amp; Afternoon Tea</p>
  <p class="times-heading">Opening Times</p>
  <div class="times"><h3>Halloways</h3><p>Monday to Saturday: 9am to 5.30pm</p></div>
  <div class="times"><h3>Cafe Lumino</h3><p>Monday to Friday : 9am to 4.30pm.<br>Saturday: 9am to 5.30pm.</p></div>
  <p class="parking">FREE PARKING</p>
  <div class="card-strip back-strip">
    <div class="panel-orange back-card">
      <span class="perforation"></span>
      <p class="address">Clara Benton<br>48 Halloways Court<br>Riverside, Melbourne, Vic, 3010</p>
      <span class="brand-name">Halloways</span>
      <p class="valid">Valid until October 30th, 2011</p>
    </div>
    <div class="panel-brown contact">
      <h4>Halloways</h4>
      <p>Harrowgate Lane (A62)<br>Elmwick<br>Bradford<br>BD12 4XY<br>PH: 01274 000 412<br>www.halloways.co.uk</p>
    </div>
  </div>
</section>

</body>
</html>
```